Wein- und Esswarenetiketten gesucht
Zielgruppe
Handel mit Getränken und Esswaren aus Italien.
Zielgruppe primär Privatpersonen, aber auch b2b (Gastronomie)
Neu möchten wir eigene Produktlinie(n) aufbauen: Rot- und Weisswein, aber auch Pasta, ...
Aufgabenstellung
Entwickeln eines einheitlichen Auftritts via Produktetiketten. Wein- und Esswarenetiketten sollen alle deutlich erkennbar sein, dasselbe Layout, denselben spirit ... zeigen. Der Kunde soll bei allen Produkten sofort an uns denken.
Bei Weinetiketten frei gestaltbar, da gesetzl. Angaben jeweils bereits auf Rückseite der Flaschen. Bei den Esswarenetiketten ev. Platz für Zusatzangaben ('Nutrifacts') zusätzlich vorsehen.
Design eher ruhig, klassisch, nicht zu verspielt. Ev. auch fast nur Worte/Text?
Keine Bilder, eher nur 'Symbole'

```html
<!DOCTYPE html>
<html lang="de">
<head>
<meta charset="utf-8">
<title>Casa Sereno – Produktetiketten</title>
<link rel="stylesheet" href="https://fonts.googleapis.com/css2?family=Mulish:wght@300;400;600&family=Kaushan+Script&display=swap">
<style>
  :root {
    --backdrop: #eeeeee;
    --gold-light: #e6d3a2;
    --gold-mid: #d4b77c;
    --gold-line: #c9a45e;
    --paper: #ffffff;
    --ink: #4a4849;
    --ink-soft: #5c5a5b;
  }
  * { box-sizing: border-box; margin: 0; padding: 0; }
  html, body {
    width: 1200px; height: 724px; overflow: hidden;
    background: var(--backdrop);
    font-family: "Mulish", Arial, sans-serif;
    color: var(--ink);
  }
  .label-set { position: relative; width: 1200px; height: 724px; }

  .pasta-band {
    position: absolute; left: 150px; top: 120px;
    width: 270px; height: 480px;
    background: linear-gradient(180deg, var(--gold-mid) 0%, var(--gold-light) 70%, #efe2bd 100%);
    display: flex; align-items: flex-end; justify-content: center;
    padding-bottom: 30px;
  }

  .wine-mount {
    position: absolute; top: 185px;
    width: 320px; height: 320px;
    background: linear-gradient(135deg, var(--gold-light) 0%, var(--gold-mid) 55%, var(--gold-light) 100%);
    display: flex; align-items: center; justify-content: center;
  }
  .wine-mount.red { left: 500px; }
  .wine-mount.white { left: 860px; }

  .label-card {
    width: 236px; height: 266px;
    background: var(--paper);
    padding: 8px;
  }
  .wine-mount .label-card { width: 260px; height: 260px; }
  .label-frame {
    width: 100%; height: 100%;
    border: 3px solid var(--gold-line);
    outline: 1px solid var(--gold-light);
    outline-offset: -7px;
    padding: 18px 20px 14px;
    display: flex; flex-direction: column;
  }
  .brand {
    font-size: 17px; font-weight: 400; text-align: center;
    letter-spacing: 0.3px; white-space: nowrap;
  }
  .rule {
    height: 1px; background: var(--ink-soft); margin-top: 9px;
  }
  .divider {
    display: flex; align-items: center; gap: 8px;
  }
  .divider::before, .divider::after {
    content: ""; flex: 1; height: 1px; background: var(--ink-soft);
  }
  .divider span { font-size: 12px; letter-spacing: 3px; line-height: 1; }
  .product {
    flex: 1; display: flex; flex-direction: column; justify-content: center;
  }
  .product-type {
    font-size: 22px; font-weight: 400; text-align: right;
    padding-right: 4px; line-height: 1;
  }
  .product-name {
    font-family: "Kaushan Script", cursive;
    font-size: 50px; line-height: 1; text-align: center;
    color: var(--ink); margin-top: 2px;
  }
  .notes-title { font-size: 9px; font-weight: 600; margin-top: 8px; }
  .notes-text { font-size: 6.5px; line-height: 1.35; }
</style>
</head>
<body>
<main class="label-set">

  <section class="pasta-band" aria-label="Etikett Farfalle Nudeln">
    <div class="label-card">
      <div class="label-frame">
        <p class="brand">Casa Sereno</p>
        <div class="rule"></div>
        <div class="product">
          <p class="product-type">Farfalle</p>
          <p class="product-name">Nudeln</p>
        </div>
        <div class="divider"><span>•••</span></div>
        <p class="notes-title">Degustationsnotizen</p>
        <p class="notes-text">Leichter, genussvoller Aperitif Wein. Helle, strohgelbe Farbe. In der Nase leicht nach Gräsern duftend.</p>
      </div>
    </div>
  </section>

  <section class="wine-mount red" aria-label="Etikett Rotwein">
    <div class="label-card">
      <div class="label-frame">
        <p class="brand">Casa Sereno</p>
        <div class="rule"></div>
        <div class="product">
          <p class="product-type">ROT</p>
          <p class="product-name">Wein</p>
        </div>
        <div class="divider"><span>•••</span></div>
        <p class="notes-title">Degustationsnotizen</p>
        <p class="notes-text">Leichter, genussvoller Aperitif Wein. Helle, strohgelbe Farbe. In der Nase leicht nach Gräsern duftend.</p>
      </div>
    </div>
  </section>

  <section class="wine-mount white" aria-label="Etikett Weisswein">
    <div class="label-card">
      <div class="label-frame">
        <p class="brand">Casa Sereno</p>
        <div class="rule"></div>
        <div class="product">
          <p class="product-type">WEISS</p>
          <p class="product-name">Wein</p>
        </div>
        <div class="divider"><span>•••</span></div>
        <p class="notes-title">Degustationsnotizen</p>
        <p class="notes-text">Leichter, genussvoller Aperitif Wein. Helle, strohgelbe Farbe. In der Nase leicht nach Gräsern duftend.</p>
      </div>
    </div>
  </section>

</main>
</body>
</html>
```